Unique and original Business Card for Financial Services Business

I have moved premises and need to change the detail on my business card so thought now is a good time for a re-design. Looking for something professional and modern with colours to fit in with out logo. Like the idea of foil or embossing if that works but not a must have but I do want something that stands out and that I could not design myself.

Once business card is designed I will also be looking to get letterhead and flyers done but want the business card concept in place first.

The majority of designs I am receiving are generic and template based. I am looking for something unique and original. We have some great design elements in our logo, think outside the box and show me something that stands out from the crowd.

Target Market(s)

Business Professionals

Industry/Entity Type

Finance

Contact Information for Business Card

Name: Delphine Moore Phone 0438 297 614 Address PO Box 7816 Ashvale NSW 2411 Email info@tidewellmoneyservices.example.com.au website www.tidewellmoneyservices.example.com.au

Font styles to use
Other font styles liked:
• Ralway

Requirements
Should not have
• No black backgrounds please

```html
<!DOCTYPE html>
<html lang="en">
<head>
<meta charset="utf-8">
<title>Tidewell Money Services – Business Card</title>
<link href="https://fonts.googleapis.com/css2?family=Montserrat:wght@500;800&family=Raleway:wght@300;500&display=swap" rel="stylesheet">
<style>
  :root {
    --stage: #e6e8ea;
    --teal: #0f9aa0;
    --teal-deep: #0b5f7a;
    --teal-dark: #0a4d66;
    --silver: #b9bcc0;
    --ink: #1c1f22;
    --paper: #ffffff;
  }
  * { margin: 0; padding: 0; box-sizing: border-box; }
  html, body { width: 1200px; height: 960px; overflow: hidden; }
  body {
    background: var(--stage);
    font-family: "Raleway", sans-serif;
    position: relative;
  }
  .card {
    position: absolute;
    left: 240px;
    width: 720px;
    height: 412px;
    border-radius: 22px;
    overflow: hidden;
    box-shadow: 0 12px 30px rgba(0,0,0,0.18);
  }
  /* Back */
  .card-back { top: 30px; background: var(--teal-deep); }
  .back-pattern {
    position: absolute; inset: 0;
    background: linear-gradient(160deg, #1a9fa6 0%, #127e93 45%, #0d6384 100%);
  }
  .back-brand {
    position: absolute;
    left: 470px; top: 168px;
    display: flex; align-items: center; gap: 8px;
    color: var(--paper);
    font-weight: 500;
    font-size: 15px;
    letter-spacing: 1px;
    text-transform: uppercase;
  }
  .back-brand .dot { width: 14px; height: 14px; border-radius: 50%; background: var(--paper); }

  /* Front */
  .card-front { top: 492px; background: var(--paper); }
  .brand {
    position: absolute;
    left: 50px; top: 100px;
    width: 300px;
    color: var(--teal);
    font-weight: 300;
  }
  .brand .mark {
    width: 64px; height: 64px; border-radius: 50%;
    background: var(--teal);
    margin: 0 auto 16px;
  }
  .brand-name {
    text-align: center;
    font-size: 30px;
    line-height: 1.1;
    letter-spacing: 1px;
    text-transform: uppercase;
  }
  .brand-sub {
    text-align: center;
    font-size: 15px;
    letter-spacing: 8px;
    margin-top: 6px;
  }
  .divider {
    position: absolute;
    left: 372px; top: 54px;
    width: 1.5px; height: 184px;
    background: var(--teal-deep);
  }
  .details {
    position: absolute;
    left: 390px; top: 50px;
    color: var(--ink);
  }
  .person-name {
    font-family: "Montserrat", sans-serif;
    font-weight: 800;
    font-size: 23px;
    letter-spacing: 0.5px;
    text-transform: uppercase;
    color: var(--teal);
  }
  .person-name .first { color: var(--teal-dark); }
  .person-role { font-family: "Montserrat", sans-serif; font-weight: 500; font-size: 14px; margin-top: 2px; }
  .address { font-family: "Montserrat", sans-serif; font-weight: 500; font-size: 14px; margin-top: 14px; line-height: 1.35; }
  .contacts { list-style: none; margin-top: 12px; font-family: "Montserrat", sans-serif; font-weight: 500; font-size: 11px; }
  .contacts li { display: flex; align-items: center; gap: 8px; height: 20px; white-space: nowrap; }
  .contacts svg { width: 13px; height: 13px; flex: none; }
  .wave { position: absolute; left: 0; bottom: 0; width: 720px; height: 412px; }
</style>
</head>
<body>

<section class="card card-back" aria-label="Card back">
  <div class="back-pattern" role="img" aria-label="Repeating monogram pattern in teal tones"></div>
  <div class="back-brand"><span class="dot"></span>Tidewell</div>
</section>

<section class="card card-front" aria-label="Card front">
  <svg class="wave" viewBox="0 0 720 412" aria-hidden="true">
    <defs>
      <linearGradient id="tealWave" x1="0" y1="1" x2="1" y2="0">
        <stop offset="0" stop-color="#0a5878"/>
        <stop offset="1" stop-color="#13a0a4"/>
      </linearGradient>
    </defs>
    <path d="M0,330 C230,410 440,290 720,256 L720,270 C450,304 240,432 0,350 Z" fill="var(--silver)"/>
    <path d="M0,358 C240,438 450,312 720,278 L720,412 L0,412 Z" fill="url(#tealWave)"/>
  </svg>

  <div class="brand">
    <div class="mark"></div>
    <div class="brand-name">Tidewell Money</div>
    <div class="brand-sub">Services</div>
  </div>

  <div class="divider"></div>

  <div class="details">
    <h1 class="person-name"><span class="first">Delphine</span> Moore</h1>
    <p class="person-role">Managing Director</p>
    <p class="address">PO Box 7816<br>Ashvale NSW 2411</p>
    <ul class="contacts">
      <li>
        <svg viewBox="0 0 24 24"><path fill="var(--teal-deep)" d="M6.6 10.8a15 15 0 0 0 6.6 6.6l2.2-2.2a1 1 0 0 1 1-.25 11.4 11.4 0 0 0 3.6.57 1 1 0 0 1 1 1V20a1 1 0 0 1-1 1A17 17 0 0 1 3 4a1 1 0 0 1 1-1h3.5a1 1 0 0 1 1 1c0 1.25.2 2.450.57 3.57a1 1 0 0 1-.25 1z"/></svg>
        0438 297 614
      </li>
      <li>
        <svg viewBox="0 0 24 24"><rect x="2" y="5" width="20" height="14" rx="1.5" fill="var(--teal-deep)"/><path d="M3 6l9 7 9-7" stroke="#fff" stroke-width="1.6" fill="none"/></svg>
        info@tidewellmoneyservices.example.com.au
      </li>
      <li>
        <svg viewBox="0 0 24 24"><circle cx="12" cy="12" r="10" fill="var(--teal-deep)"/><path d="M2 12h20M12 2c3 3 3 17 0 20M12 2c-3 3-3 17 0 20" stroke="#fff" stroke-width="1.3" fill="none"/></svg>
        www.tidewellmoneyservices.example.com.au
      </li>
    </ul>
  </div>
</section>

</body>
</html>
```